Adorable Luxury Flower Shop

Need a beautiful, eye catching, elegant full-service website.
INSPIRATIONS ARE;
https://www.quillmoreblooms.com

Industry/Entity Type

retail, floral, boutique

Coding

Coded - Design and coding required

Number of Pages Required

3 page

Requirements
Must have
• SEO, Coded, UX, Fully responsive mobile, tablet, desktop, Ecommerce setup with Square, payments integration (if we use squarespace). SEO optimization with keywords, tags, meta descriptions, Load speed optimization, Google my business setup.
Nice to have
• pictures, color, elegance

```html
<!DOCTYPE html>
<html lang="en">
<head>
<meta charset="utf-8">
<title>Rosemere Flower Boutique</title>
<link rel="stylesheet" href="https://fonts.googleapis.com/css2?family=Playfair+Display:wght@400;600;700&family=Poppins:wght@400;500;600&display=swap">
<style>
:root{
  --bg:#efebe8;
  --red:#b81c1f;
  --ink:#1b1b1b;
  --muted:#555;
  --white:#ffffff;
  --line:#c9c4c0;
}
*{margin:0;padding:0;box-sizing:border-box}
html,body{width:1200px;height:4886px;overflow:hidden}
body{background:var(--bg);color:var(--ink);font-family:'Poppins',sans-serif;position:relative}
.abs{position:absolute}
.red{color:var(--red)}

/* header */
.header{top:0;left:0;width:1200px;height:154px;background:var(--bg);z-index:2}
.brand-disc{left:475px;top:10px;width:250px;height:180px;border-radius:50%;background:var(--bg);z-index:3}
.brand-name{left:475px;top:72px;width:250px;text-align:center;font-family:'Playfair Display',serif;font-weight:700;font-size:40px;color:var(--ink);z-index:4}
.call{left:128px;top:38px;font-size:14px;font-weight:600;display:flex;align-items:center;gap:10px}
.nav a{position:absolute;top:106px;font-size:13px;font-weight:600;color:var(--ink);text-decoration:none}
.account{left:900px;top:40px;font-size:14px;font-weight:600;display:flex;align-items:center;gap:12px}

/* hero */
.hero{top:154px;left:0;width:1200px;height:586px;background:linear-gradient(120deg,#5a4a45 0%,#a8405c 35%,#c7577c 55%,#8e6a9c 75%,#b5b050 100%)}
.hero-title{left:125px;top:462px;font-family:'Playfair Display',serif;font-weight:700;font-size:80px;color:var(--white);line-height:1}
.hero-sub{left:125px;top:552px;font-size:36px;font-weight:600;color:var(--white);letter-spacing:1px}
.btn{background:var(--red);color:var(--white);display:flex;align-items:center;justify-content:center;font-weight:700;text-decoration:none}
.hero-btn{left:127px;top:622px;width:233px;height:48px;font-family:'Playfair Display',serif;font-size:13px;letter-spacing:.5px}

/* categories */
.cat{top:766px;width:366px;height:432px}
.cat-label{position:absolute;left:98px;top:191px;width:170px;height:57px;background:var(--bg);border:3px double #555;display:flex;align-items:center;justify-content:center;font-family:'Playfair Display',serif;font-weight:700;font-size:24px}

/* section titles */
.ornament{width:150px;height:52px;left:525px;background:linear-gradient(#3a3a3a,#3a3a3a) center/100% 2px no-repeat}
.sec-title{left:0;width:1200px;text-align:center;font-family:'Playfair Display',serif;font-weight:700;font-size:48px}

/* carousel */
.card{top:1452px;width:234px;height:277px}
.caption{top:1745px;width:234px;text-align:center;font-size:15px;color:var(--muted)}
.arrow{top:1570px;width:42px;height:42px;border:2px solid var(--ink);border-radius:50%;display:flex;align-items:center;justify-content:center}
.cta{top:1826px;left:482px;width:237px;height:47px;font-size:17px}

.rule{left:0;width:1200px;height:2px;background:var(--line)}

/* about */
.about-title{top:1975px}
.about-text{left:265px;top:2072px;width:670px;text-align:center;font-size:15px;line-height:24px;color:#333}

/* owner */
.owner{top:2281px;left:0;width:1200px;height:546px;background:linear-gradient(90deg,#8a7a70 0%,#6a5a55 45%,#7a5560 70%,#8d3d45 100%)}
.owner-title{left:681px;top:2358px;font-family:'Playfair Display',serif;font-weight:600;font-size:56px;color:var(--white)}
.owner-text{left:681px;top:2440px;width:430px;font-size:15px;line-height:24px;color:var(--white)}

/* classes */
.class-kicker{left:120px;top:3000px;font-family:'Playfair Display',serif;font-size:18px;color:#888}
.class-title{left:120px;top:3022px;font-family:'Playfair Display',serif;font-weight:700;font-size:40px}
.class-text{left:120px;top:3092px;width:452px;font-size:15px;line-height:24px;color:#333}
.email-box{left:119px;top:3293px;width:228px;height:51px;background:var(--white);font-size:13px;padding:17px 18px;color:#333}
.signup{left:362px;top:3293px;width:131px;height:51px;font-family:'Playfair Display',serif;font-size:16px}
.class-photo{left:603px;top:2960px;width:510px;height:413px;background:linear-gradient(135deg,#6a5e9a 0%,#c14e78 40%,#e48aa4 60%,#8a9a6a 100%)}

/* social gallery */
.gallery{top:3711px;width:233px;height:269px}
.follow{left:491px;top:4021px;width:216px;height:61px;font-family:'Playfair Display',serif;font-size:14px}

/* newsletter */
.band{left:0;top:4201px;width:1200px;height:258px;background:var(--red)}
.rose{left:548px;top:4163px;width:82px;height:74px;border-radius:50%;background:var(--red);border:3px solid var(--bg);z-index:2}
.band-title{left:0;top:4240px;width:1200px;text-align:center;font-family:'Playfair Display',serif;font-weight:600;font-size:40px;color:var(--white)}
.band-text{left:0;top:4306px;width:1200px;text-align:center;font-size:15px;line-height:23px;color:var(--white)}
.band-email{left:408px;top:4374px;width:384px;height:36px;border-bottom:1px solid var(--white);font-size:14px;color:var(--white);display:flex;justify-content:space-between;align-items:center}

/* footer */
.foot-brand{left:117px;top:4594px;width:234px;text-align:center;font-family:'Playfair Display',serif;font-weight:700;font-size:36px}
.foot-h{top:4530px;font-family:'Playfair Display',serif;font-weight:700;font-size:22px}
.foot-list{font-size:14px;line-height:29.5px;color:#333;list-style:none}
.contact-item{left:593px;display:flex;gap:14px;font-size:14px;line-height:19px;color:#333}
.pin{width:36px;height:36px;border-radius:50%;background:var(--red);display:flex;align-items:center;justify-content:center;flex:none}
.social{top:4710px;width:34px;height:34px;border-radius:50%}
.copy{left:201px;top:4802px;width:798px;height:84px;background:var(--red);border-radius:60px 60px 0 0;color:var(--white);font-size:14px;text-align:center;padding-top:24px}
</style>
</head>
<body>

<header class="abs header">
  <div class="call abs">
    <svg width="26" height="26" viewBox="0 0 24 24" fill="none" stroke="#1b1b1b" stroke-width="1.6"><path d="M5 3h4l2 5-2.5 1.5a11 11 0 0 0 6 6L16 13l5 2v4a2 2 0 0 1-2 2A17 17 0 0 1 3 5a2 2 0 0 1 2-2z"/></svg>
    Call: 555 214 3870
  </div>
  <nav class="nav">
    <a style="left:122px">FLOWERS</a>
    <a style="left:238px">GIFTS</a>
    <a style="left:328px">BY OCCASION</a>
    <a style="left:777px">EVENTS</a>
    <a style="left:880px">ABOUT US</a>
    <a style="left:1004px">CONTACT</a>
  </nav>
  <div class="account abs">
    My Account
    <svg width="26" height="28" viewBox="0 0 24 26" fill="none" stroke="#1b1b1b" stroke-width="1.6"><circle cx="12" cy="8" r="5"/><path d="M2 25c1-6 5-9 10-9s9 3 10 9"/></svg>
    <svg width="26" height="32" viewBox="0 0 24 30" fill="none" stroke="#b81c1f" stroke-width="1.8"><rect x="2" y="8" width="20" height="20" rx="2"/><path d="M7 8V6a5 5 0 0 1 10 0v2"/><circle cx="12" cy="18" r="4"/></svg>
  </div>
</header>
<div class="abs brand-disc"></div>
<div class="abs brand-name">ROSEMERE</div>

<section class="abs hero" role="img" aria-label="Close-up photo of a bouquet of roses, lisianthus and carnations"></section>
<h1 class="abs hero-title">Rosemere</h1>
<div class="abs hero-sub">FLOWER BOUTIQUE</div>
<a class="abs btn hero-btn">VIEW OUR COLLECTION</a>

<div class="abs cat" style="left:25px;background:linear-gradient(135deg,#7a1a3a,#c2306a 50%,#d88a30)" role="img" aria-label="Photo of dahlias and lilies"><div class="cat-label">Florals</div></div>
<div class="abs cat" style="left:417px;background:linear-gradient(160deg,#4a5a3a,#2e6a6a 55%,#8aa06a)" role="img" aria-label="Photo of potted succulents"><div class="cat-label">Botanicals</div></div>
<div class="abs cat" style="left:810px;background:linear-gradient(160deg,#b89a6a,#d8ccb0 55%,#e8e2d6)" role="img" aria-label="Photo of a wine bottle with white flowers"><div class="cat-label">Wines</div></div>

<div class="abs ornament" style="top:1304px" role="img" aria-label="Ornamental flourish"></div>
<h2 class="abs sec-title" style="top:1352px">Floral <span class="red">Designs</span></h2>

<div class="abs arrow" style="left:32px"><svg width="14" height="14" viewBox="0 0 14 14" fill="none" stroke="#1b1b1b" stroke-width="2"><path d="M9 2 4 7l5 5"/></svg></div>
<div class="abs arrow" style="left:1122px"><svg width="14" height="14" viewBox="0 0 14 14" fill="none" stroke="#1b1b1b" stroke-width="2"><path d="M5 2l5 5-5 5"/></svg></div>
<div class="abs card" style="left:102px;background:linear-gradient(160deg,#6a5040,#e0a8a0 50%,#7a9a8a)" role="img" aria-label="Photo of a pastel rose bouquet"></div>
<div class="abs card" style="left:356px;background:linear-gradient(160deg,#e8e4e0,#e86a30 45%,#d8c040)" role="img" aria-label="Photo of gerbera daisies in a vase"></div>
<div class="abs card" style="left:610px;background:linear-gradient(160deg,#3a2a20,#c0302a 40%,#f0eeea 70%,#3a4a3a)" role="img" aria-label="Photo of white and red flowers in a pot"></div>
<div class="abs card" style="left:863px;background:linear-gradient(160deg,#e8e6e2,#9a5aa8 45%,#6a8a5a)" role="img" aria-label="Photo of purple tulips in a glass vase"></div>
<div class="abs caption" style="left:102px">Floral Name</div>
<div class="abs caption" style="left:356px">Floral Name</div>
<div class="abs caption" style="left:610px">Floral Name</div>
<div class="abs caption" style="left:863px">Floral Name</div>
<a class="abs btn cta">View Our Collection</a>

<div class="abs rule" style="top:1926px"></div>

<h2 class="abs sec-title about-title" style="font-size:56px">About Rosemere</h2>
<p class="abs about-text">Lorem ipsum dolor sit amet, consectetur adipiscing elit, sed do eiusmod tempor incid dunt ut labore et dolore magna aliqua. Quis ipsum suspendisse ultrices gravida. Risus commodo viverra maecenas accumsan lacus vel facilisis. Lorem ipsum dolorsit amet, consectetur adipiscing elit, sed do eiusmod tem por incididunt .</p>

<section class="abs owner" role="img" aria-label="Photo of the florist arranging white and red roses in her shop"></section>
<h2 class="abs owner-title">About Owner</h2>
<p class="abs owner-text">Lorem ipsum dolor sit amet, consectetur adipiscing elit, sed do eiusmod tempor incididunt ut labore et dolore magna aliqua. Quis ipsum suspendisse ultrices gravida. Risus commodo viverra maecenas accumsan.</p>

<div class="abs class-kicker">Upcoming Classes</div>
<h2 class="abs class-title">WIne and Design</h2>
<p class="abs class-text">Lorem ipsum dolor sit amet, consectetur adipiscing elit, sed do eiusmod tempor incididunt ut labore et dolre ma gna aliqua. Quis ipsum suspendisse ultrices gravida. Risus commodo viverra maecenas accumsan lacus vel facilisis. sus endisse ultrices gravida. Risus commodo viverra maec enas accumsan lacus vel facilLorem ipsum dolor sime. Lecenas accumsan lacus vel facilisis.</p>
<div class="abs email-box">Email:</div>
<a class="abs btn signup">Sign Up</a>
<div class="abs class-photo" role="img" aria-label="Photo of a peony and delphinium arrangement in a glass vase"></div>

<div class="abs rule" style="top:3485px"></div>

<div class="abs ornament" style="top:3568px" role="img" aria-label="Ornamental flourish"></div>
<h2 class="abs sec-title" style="top:3616px">Find us <span class="red">on Social</span></h2>
<div class="abs gallery" style="left:95px;background:linear-gradient(160deg,#e8c8c0,#d89890 50%,#6a4aa0)" role="img" aria-label="Photo of a pink rose gift box"></div>
<div class="abs gallery" style="left:351px;background:linear-gradient(160deg,#d8c8b8,#c88a90 50%,#8a9a6a)" role="img" aria-label="Photo of a dusty pink arrangement"></div>
<div class="abs gallery" style="left:607px;background:linear-gradient(160deg,#d84a3a,#e8a040 45%,#6a5ab0)" role="img" aria-label="Photo of a bright mixed bouquet"></div>
<div class="abs gallery" style="left:861px;background:linear-gradient(160deg,#f0eeea,#d8d6d0 50%,#8a9a7a)" role="img" aria-label="Photo of a white bridal bouquet"></div>
<a class="abs btn follow">FOLLOW US ON</a>

<section class="abs band"></section>
<div class="abs rose" role="img" aria-label="Rose emblem"></div>
<h2 class="abs band-title">Stay in Rosemere Flower Boutique</h2>
<p class="abs band-text">Join our exclusive list and be the first to know about new collections,<br>special offers, and insider tips from Rosemere Flower Boutique.</p>
<div class="abs band-email">Email Id
  <svg width="30" height="14" viewBox="0 0 30 14" fill="none" stroke="#fff" stroke-width="2"><path d="M0 7h28M22 1l6 6-6 6"/></svg>
</div>

<div class="abs foot-brand">ROSEMERE</div>

<h3 class="abs foot-h" style="left:410px">Company</h3>
<ul class="abs foot-list" style="left:410px;top:4575px">
  <li>About Us</li><li>Blog</li><li>Contact Us</li><li>Privacy Policy</li><li>Refund Policy</li>
</ul>

<h3 class="abs foot-h" style="left:593px">Contact</h3>
<div class="abs contact-item" style="top:4583px">
  <span class="pin"><svg width="16" height="20" viewBox="0 0 16 20" fill="#fff"><path d="M8 0a7 7 0 0 0-7 7c0 5 7 13 7 13s7-8 7-13a7 7 0 0 0-7-7zm0 10a3 3 0 1 1 0-6 3 3 0 0 1 0 6z"/></svg></span>
  <span>Location 1:<br>72 Garden Row</span>
</div>
<div class="abs contact-item" style="top:4655px">
  <span class="pin"><svg width="18" height="18" viewBox="0 0 24 24" fill="#fff"><path d="M5 3h4l2 5-2.5 1.5a11 11 0 0 0 6 6L16 13l5 2v4a2 2 0 0 1-2 2A17 17 0 0 1 3 5a2 2 0 0 1 2-2z"/></svg></span>
  <span>Phone:<br>555 306 1142</span>
</div>

<h3 class="abs foot-h" style="left:853px">Store Hours</h3>
<ul class="abs foot-list" style="left:853px;top:4575px">
  <li>Monday - Friday 9am - 4pm</li><li>Saturday - 10am - 4pm</li><li>Sunday - 11am - 4pm</li><li>Closed on all Public Holidays</li>
</ul>
<div class="abs social" style="left:848px;background:var(--red)"></div>
<div class="abs social" style="left:887px;background:var(--ink)"></div>
<div class="abs social" style="left:927px;background:var(--ink)"></div>
<div class="abs social" style="left:967px;background:var(--ink)"></div>

<footer class="abs copy">Copyright © 2025 All rights reserved - Rosemere Flower Boutique. Terms &amp; Conditions</footer>

</body>
</html>
```